HRW / PFB

I need a business card for the owner of sister companies. Please see minimalist version of our old business card for just the Halvorsen business. We need to now have a card that shows off both the Halvorsen logo and the Pale Fern Builders logo. We would like the aesthetic to go well with our brand, and not differ greatly from our Halvorsen cards. These companies are sister companies, there is not one parent company. Looking for a visually appealing design, but not sure if it should be diagonal or something to make it visually attractive... or just some other type of divider. We prefer white logos with a blue background. White transparent background png logos are attached. Please use blue background with hex code 566b7c. The person and contact information will be on the back side, and I can do that myself. We will NOT need to add the text for design-build-sales-installation.

```html
<!DOCTYPE html>
<html lang="en">
<head>
<meta charset="utf-8">
<title>Pale Fern Builders &amp; Halvorsen — Business Card</title>
<link href="https://fonts.googleapis.com/css2?family=Montserrat:wght@300;400;600;700;800&display=swap" rel="stylesheet">
<style>
  :root {
    --card-blue: #566b7c;
    --ink: #ffffff;
    --ink-soft: rgba(255,255,255,0.88);
    --backdrop: #1f2023;
  }
  * { margin: 0; padding: 0; box-sizing: border-box; }
  html, body { width: 1200px; height: 1048px; overflow: hidden; }
  body {
    background: var(--backdrop);
    font-family: "Montserrat", Arial, sans-serif;
    color: var(--ink);
    position: relative;
  }
  .card {
    position: absolute;
    background: var(--card-blue);
    border-radius: 24px;
    overflow: hidden;
  }

  /* Front side: landscape */
  .card-front {
    left: 70px; top: 330px;
    width: 640px; height: 370px;
  }
  .brand-main {
    position: absolute;
    left: 150px; top: 96px;
    width: 300px;
    text-align: center;
  }
  .brand-main .brand-initials {
    display: block;
    font-weight: 800;
    font-size: 104px;
    line-height: 1;
    letter-spacing: 2px;
  }
  .brand-main .brand-name {
    display: block;
    margin-top: 10px;
    font-weight: 700;
    font-size: 24px;
    letter-spacing: 0.2px;
  }
  .brand-sister {
    position: absolute;
    right: 36px; bottom: 40px;
    display: flex; align-items: center; gap: 10px;
  }
  .brand-sister .mark-square {
    width: 34px; height: 34px; background: var(--ink);
  }
  .brand-sister .sister-text { line-height: 1.1; }
  .brand-sister .sister-name { font-weight: 700; font-size: 15px; display: block; }
  .brand-sister .sister-tag { font-weight: 400; font-size: 10px; display: block; }

  /* Back side: portrait */
  .card-back {
    left: 780px; top: 200px;
    width: 370px; height: 640px;
    text-align: center;
  }
  .back-brands {
    position: absolute; top: 64px; left: 0; right: 0;
    display: flex; justify-content: center; align-items: center; gap: 18px;
    font-weight: 800; font-size: 20px;
  }
  .back-brands .mark-square { width: 20px; height: 20px; background: var(--ink); display: inline-block; vertical-align: middle; margin-right: 6px; }
  .person {
    position: absolute; top: 130px; left: 0; right: 0;
  }
  .person-name {
    font-weight: 700; font-size: 30px; letter-spacing: 2.5px;
    text-transform: uppercase;
  }
  .person-title {
    font-weight: 400; font-size: 18px; margin-top: 4px;
  }
  .contact-group {
    position: absolute; left: 0; right: 0;
    font-weight: 300; font-size: 17px; line-height: 1.45;
    color: var(--ink-soft);
  }
  .contact-group.pfb { top: 262px; }
  .contact-group.halvorsen { top: 442px; }
  .contact-icons {
    display: flex; justify-content: center; align-items: center; gap: 5px;
    margin-bottom: 16px;
  }
  .contact-icons .rule { width: 14px; height: 1.5px; background: var(--ink); margin: 0 6px; }
  .contact-icons svg { width: 20px; height: 20px; }
</style>
</head>
<body>

  <section class="card card-front" aria-label="Card front">
    <div class="brand-main">
      <span class="brand-initials">PFB</span>
      <span class="brand-name">pale fern builders</span>
    </div>
    <div class="brand-sister">
      <span class="mark-square"></span>
      <span class="sister-text">
        <span class="sister-name">halvorsen+co</span>
        <span class="sister-tag">kitchen+bath</span>
      </span>
    </div>
  </section>

  <section class="card card-back" aria-label="Card back">
    <div class="back-brands">
      <span>PFB</span>
      <span><span class="mark-square"></span>Halvorsen</span>
    </div>

    <div class="person">
      <div class="person-name">Owen Castell</div>
      <div class="person-title">Founder &amp; CEO</div>
    </div>

    <div class="contact-group pfb">
      <div class="contact-icons">
        <span class="rule"></span>
        <svg viewBox="0 0 20 20" aria-hidden="true"><rect width="20" height="20" rx="5" fill="#fff"/><path d="M6 5.5l2 0 1 3-1.3 1a6 6 0 0 0 2.8 2.8l1-1.3 3 1v2a1 1 0 0 1-1 1A9 9 0 0 1 5 6.5a1 1 0 0 1 1-1z" fill="#566b7c"/></svg>
        <svg viewBox="0 0 20 20" aria-hidden="true"><rect width="20" height="20" rx="5" fill="#fff"/><rect x="4.5" y="6" width="11" height="8" rx="1" fill="none" stroke="#566b7c" stroke-width="1.5"/><path d="M4.8 6.5l5.2 4 5.2-4" fill="none" stroke="#566b7c" stroke-width="1.5"/></svg>
        <svg viewBox="0 0 20 20" aria-hidden="true"><rect width="20" height="20" rx="5" fill="#fff"/><circle cx="10" cy="10" r="5" fill="none" stroke="#566b7c" stroke-width="1.5"/><path d="M5 10h10M10 5c-2.5 3-2.5 7 0 10M10 5c2.5 3 2.5 7 0 10" fill="none" stroke="#566b7c" stroke-width="1.2"/></svg>
        <span class="rule"></span>
      </div>
      <div>(555) 018-2746</div>
      <div>info@palefernbuilders.com</div>
      <div>palefernbuilders.com</div>
    </div>

    <div class="contact-group halvorsen">
      <div class="contact-icons">
        <span class="rule"></span>
        <svg viewBox="0 0 20 20" aria-hidden="true"><rect width="20" height="20" rx="5" fill="#fff"/><path d="M6 5.5l2 0 1 3-1.3 1a6 6 0 0 0 2.8 2.8l1-1.3 3 1v2a1 1 0 0 1-1 1A9 9 0 0 1 5 6.5a1 1 0 0 1 1-1z" fill="#566b7c"/></svg>
        <svg viewBox="0 0 20 20" aria-hidden="true"><rect width="20" height="20" rx="5" fill="#fff"/><rect x="4.5" y="6" width="11" height="8" rx="1" fill="none" stroke="#566b7c" stroke-width="1.5"/><path d="M4.8 6.5l5.2 4 5.2-4" fill="none" stroke="#566b7c" stroke-width="1.5"/></svg>
        <svg viewBox="0 0 20 20" aria-hidden="true"><rect width="20" height="20" rx="5" fill="#fff"/><circle cx="10" cy="10" r="5" fill="none" stroke="#566b7c" stroke-width="1.5"/><path d="M5 10h10M10 5c-2.5 3-2.5 7 0 10M10 5c2.5 3 2.5 7 0 10" fill="none" stroke="#566b7c" stroke-width="1.2"/></svg>
        <span class="rule"></span>
      </div>
      <div>(555) 018-2746</div>
      <div>info@halvorsenplusco.com</div>
      <div>halvorsenplusco.com</div>
    </div>
  </section>

</body>
</html>
```